Corvane Holdings needs a business card

I would like the card to be simple but modern and elegant.
I like black and white.
or black and gold.
we are a private finance lender and also are involved in property and property developments.

please look at the business card photos i provided i would like C.H only one one side and all the other details on the other side use fonts that tie in with my theme.

Industry/Entity Type

Finance

Contact Information for Business Card

Corvane Holdings (C.H) Elliot Marbury M: 0413586102 E: elliotmar@examplemail.net

Font styles to use
Other font styles liked:
• Use fonts that would reflect our business

Colors
000000
ffffff

Requirements
Must have
• one side of details
• other side has either C.H or Corvane Holdings like in the photos provided

```html
<!DOCTYPE html>
<html lang="en">
<head>
<meta charset="utf-8">
<title>Corvane Holdings — Business Card</title>
<link rel="stylesheet" href="https://fonts.googleapis.com/css2?family=Lato:wght@300;400&display=swap">
<style>
  :root {
    --ink: #000000;
    --paper: #ffffff;
    --backdrop: #ecebe8;
    --card-shadow: rgba(0, 0, 0, 0.18);
  }
  html, body {
    margin: 0;
    padding: 0;
    overflow: hidden;
  }
  body {
    width: 1200px;
    height: 512px;
    background: var(--backdrop);
    font-family: "Lato", "Helvetica Neue", Arial, sans-serif;
    font-weight: 300;
    color: var(--paper);
  }
  .card-set {
    display: flex;
    justify-content: center;
    align-items: center;
    gap: 60px;
    height: 100%;
  }
  .card {
    position: relative;
    width: 490px;
    height: 280px;
    background: var(--ink);
    box-shadow: 0 10px 28px var(--card-shadow);
    box-sizing: border-box;
  }
  .card-front__company {
    position: absolute;
    top: 16px;
    left: 18px;
    margin: 0;
    font-size: 15px;
    letter-spacing: 0.2px;
  }
  .card-front__details {
    position: absolute;
    top: 112px;
    left: 0;
    right: 0;
    text-align: center;
  }
  .card-front__name {
    margin: 0;
    font-size: 21px;
    letter-spacing: 0.4px;
  }
  .card-front__rule {
    width: 190px;
    height: 1.5px;
    margin: 6px auto 6px;
    background: var(--paper);
    border: 0;
  }
  .card-front__contact {
    margin: 0;
    font-size: 15px;
    line-height: 1.3;
  }
  .card-back {
    display: flex;
    align-items: center;
    justify-content: center;
  }
  .card-back__monogram {
    margin: 0;
    font-size: 60px;
    font-weight: 300;
    letter-spacing: 4px;
  }
</style>
</head>
<body>
  <main class="card-set">
    <section class="card card-front" aria-label="Card front with contact details">
      <p class="card-front__company">Corvane Holdings (C.H)</p>
      <div class="card-front__details">
        <p class="card-front__name">Elliot Marbury</p>
        <hr class="card-front__rule">
        <p class="card-front__contact">M: 0413586102</p>
        <p class="card-front__contact">E: elliotmar@examplemail.net</p>
      </div>
    </section>
    <section class="card card-back" aria-label="Card back with initials">
      <p class="card-back__monogram">C.H</p>
    </section>
  </main>
</body>
</html>
```